Package Storage Service

Ideas...

Business Name... "TUCK IT AT BRAMWOOD":
Store it,
Don’t Ship it;
4-LESS
Convenience, Quality, Service

Easy as ABC…
A. Contact Us 064-293-5527
B. We deliver
C. We pick-up & Store

LESS, is the new MORE

Box Size* (Approx) Weight Limit Price per Month
41 cm X 34 cm X 26 cm 10 Kilos 12 CHFs/per month
48 cm X 43 cm X 35 cm 25 Kilos 25 CHFs/per month

* Larger sizes and prices available upon request.

Contact: Tom /064-293-5527

These are only ideas for a small package storage service for local college students. The storage times are usually for 1 - 3 months.
I need a catchy, creative, colorful design for a new business.

This flyer will need to be printable in color. A-4 size or 8 1/2 " X 11".

Target Market(s)

Hotel Management students leaving their program for vacations for short terms. They return after vacation or after practical work experiences 4 study.

Industry/Entity Type

College

Requirements
Must have
• Prices, box sizes, catchy format.

Idea will forward to their address should they not return to the school; for a postage fee + 15.00 CHFs.

Contact information for the PICKUP and DELIVERY Service... see above.

Include a PICKUP AND DELIVERY Option in the flyer.
Nice to have
• Colorful boxes with a creative idea for someone to choose spending a little each month rather than a lot at one time. 25 CHFs rather than 125 CHFs.
Should not have
• Not too wordy.

```html
<!DOCTYPE html>
<html lang="en">
<head>
<meta charset="utf-8">
<title>Tuck It At Bramwood – Package Storage Flyer</title>
<link rel="stylesheet" href="https://fonts.googleapis.com/css2?family=Roboto+Condensed:wght@700;800&family=Open+Sans:wght@400;600;700&display=swap">
<style>
  :root {
    --backdrop: #ececec;
    --green: #8cc63f;
    --blue-deep: #1b5cab;
    --blue-mid: #29abe2;
    --blue-light: #a9daf3;
    --blue-pale: #c8e5f6;
    --white: #ffffff;
    --ink: #1f1f1f;
    --black: #111111;
    --photo-top: #f3f1ee;
    --photo-bottom: #c9a57a;
  }
  * { box-sizing: border-box; margin: 0; padding: 0; }
  html, body { width: 1200px; height: 900px; overflow: hidden; }
  body { background: var(--backdrop); position: relative; }

  .flyer {
    position: absolute; left: 305px; top: 31px;
    width: 590px; height: 838px;
    background: var(--green); overflow: hidden;
    font-family: "Open Sans", Arial, sans-serif;
    box-shadow: 0 4px 14px rgba(0,0,0,.18);
  }
  .flyer-art { position: absolute; inset: 0; }

  .brand-bubble {
    position: absolute; left: -40px; top: -60px; width: 245px; height: 192px;
    border-radius: 50%; background: var(--blue-pale);
  }
  .brand-name {
    position: absolute; left: 28px; top: 30px; width: 170px;
    font-family: "Roboto Condensed", "Arial Narrow", sans-serif;
    font-weight: 800; font-size: 26px; line-height: 1.15;
    color: var(--blue-deep); text-align: center;
  }

  .pickup-badge {
    position: absolute; left: 45px; top: 340px; width: 144px; height: 144px;
    border-radius: 50%; background: var(--black);
    display: flex; align-items: center; justify-content: center;
  }
  .pickup-badge span {
    width: 124px; height: 124px; border-radius: 50%;
    background: var(--blue-mid); color: var(--white);
    display: flex; align-items: center; justify-content: center; text-align: center;
    font-family: "Roboto Condensed", "Arial Narrow", sans-serif;
    font-weight: 700; font-size: 22px; line-height: 1.3;
    transform: rotate(-8deg);
  }

  .box-tiles {
    position: absolute; left: 351px; top: 410px;
    display: grid; grid-template-columns: 106px 107px; gap: 4px 6px;
  }
  .box-tile {
    height: 80px; background: var(--white); border-radius: 12px;
    display: flex; align-items: center; justify-content: center;
  }
  .box-tile i { display: block; width: 52px; height: 54px; border-radius: 4px; }
  .box-tile .grey { background: linear-gradient(#ffffff, #c9c9c9); }
  .box-tile .yellow { background: linear-gradient(#ffe26a, #f2b705); }
  .box-tile .kraft { background: linear-gradient(#e8b77e, #b97c3e); }
  .box-tile .pink { background: linear-gradient(#f47ab8, #d6267f); }

  .headline {
    position: absolute; left: 27px; top: 504px;
    font-family: "Roboto Condensed", "Arial Narrow", sans-serif;
    color: var(--white);
  }
  .headline h1 { font-weight: 800; font-size: 35px; line-height: 1.1; }
  .headline p { font-weight: 700; font-size: 20px; line-height: 1.2; }

  .price-table {
    position: absolute; left: 15px; top: 580px; width: 565px;
    border-collapse: collapse; color: var(--ink); font-size: 17px; line-height: 21px;
  }
  .price-table th { font-weight: 700; text-align: center; padding: 0; }
  .price-table td { text-align: center; padding: 0; }

  .box-stack {
    position: absolute; left: 23px; top: 652px; width: 268px; height: 100px;
    background: linear-gradient(90deg, #f27a1a 0 32%, #e8398a 32% 50%, #3ab6c8 50% 64%, #4a4a4a 64%);
    border-radius: 6px;
  }

  .request-note {
    position: absolute; left: 25px; top: 755px; height: 56px;
    border-left: 8px solid var(--blue-mid); padding-left: 10px;
    font-family: "Roboto Condensed", "Arial Narrow", sans-serif;
    font-weight: 700; font-size: 21px; line-height: 27px; color: var(--white);
  }

  .contact-panel {
    position: absolute; left: 318px; top: 736px; width: 260px;
    font-family: "Roboto Condensed", "Arial Narrow", sans-serif;
    font-weight: 700; font-size: 19px; line-height: 27px;
    color: var(--white); text-align: center;
  }
</style>
</head>
<body>
  <main class="flyer">
    <svg class="flyer-art" width="590" height="838" viewBox="0 0 590 838" aria-hidden="false">
      <defs>
        <linearGradient id="photoTone" x1="0" y1="0" x2="0" y2="1">
          <stop offset="0" stop-color="var(--photo-top)"/>
          <stop offset="1" stop-color="var(--photo-bottom)"/>
        </linearGradient>
      </defs>
      <g class="header-waves">
        <path fill="var(--blue-mid)" d="M0 0 H590 V288 C480 348 360 378 295 448 C230 378 110 348 0 288 Z"/>
        <path fill="var(--white)" d="M0 0 H590 V276 C480 336 360 366 295 436 C230 366 110 336 0 276 Z"/>
        <path fill="var(--blue-light)" d="M0 0 H590 V266 C480 326 360 356 295 426 C230 356 110 326 0 266 Z"/>
        <path fill="var(--blue-deep)" d="M0 0 H590 V254 C480 314 360 344 295 414 C230 344 110 314 0 254 Z"/>
      </g>
      <path role="img" aria-label="Photo of two smiling students carrying cardboard moving boxes"
            fill="url(#photoTone)" d="M0 0 H590 V240 C480 300 360 330 295 400 C230 330 110 300 0 240 Z"/>
      <g class="footer-oval">
        <ellipse cx="500" cy="770" rx="220" ry="100" fill="var(--blue-deep)"/>
        <ellipse cx="505" cy="775" rx="212" ry="90" fill="var(--blue-light)"/>
        <ellipse cx="510" cy="782" rx="208" ry="84" fill="var(--blue-mid)"/>
      </g>
    </svg>

    <div class="brand-bubble"></div>
    <div class="brand-name">TUCK IT AT<br>BRAMWOOD</div>

    <div class="pickup-badge"><span>Pickup<br>and<br>Delivery</span></div>

    <div class="box-tiles">
      <div class="box-tile"><i class="grey" role="img" aria-label="Illustration of an open white box"></i></div>
      <div class="box-tile"><i class="yellow" role="img" aria-label="Illustration of an open yellow box"></i></div>
      <div class="box-tile"><i class="kraft" role="img" aria-label="Illustration of an open cardboard box"></i></div>
      <div class="box-tile"><i class="pink" role="img" aria-label="Illustration of an open pink box"></i></div>
    </div>

    <div class="headline">
      <h1>Store it, Don’t Ship it</h1>
      <p>Convenience,Quality, Service</p>
    </div>

    <table class="price-table">
      <tr><th>Box Size</th><th>Weight Limit</th><th>Price Per Month</th></tr>
      <tr><td>41 cm X 34 cm X 26 cm</td><td>10 Kilos</td><td>12 CHFs/Per Month</td></tr>
      <tr><td>48 cm X 43 cm X 35 cm</td><td>25 Kilos</td><td>25 CHFs/ Per Month</td></tr>
    </table>

    <div class="box-stack" role="img" aria-label="Illustration of colourful storage boxes in orange, pink, teal and grey"></div>

    <div class="request-note">Larzer Sizes and Prices<br>Available Upon Request</div>

    <div class="contact-panel">
      Contact Us 064-293-5527<br>
      Contact : Tom / 064-293-5527
    </div>
  </main>
</body>
</html>
```